Sleek & Sexy MedSpa Direct Mailer Needed for High End Client

We need an eye catching and elegant direct mailer for our client Corva Lune Medical Spa. Please stay with black & white tones. They like Tessa Brimlow brand looks - sleek & sexy & high end.

Here is the template layout: https://quillvane.com/offering/coupon-mailer you can download a PDF or IDML on that page.

Website: https://corvalunemedicalspa.com/
Logo: https://files.dorvex.com/folders/7kqPz3Rt9Wm2Lx8Vb4Nc6Yh1Jd5Gs0FaE

Offers:
New Year/ New You! Make your beauty dreams a reality!
15% off laser hair removal packages
$50 off Velquin or Parelle
$75 off 1 Filler syringe
15% off KX products

Call today to learn more & make sure to mention MAIL OFFER!

```html
<!DOCTYPE html>
<html lang="en">
<head>
<meta charset="utf-8">
<title>Corva Lune Medical Spa – New Year Mailer</title>
<link rel="stylesheet" href="https://fonts.googleapis.com/css2?family=Montserrat:wght@300;400;500;600;800;900&family=Poppins:wght@300;400&display=swap">
<style>
:root{
  --bg:#c9c9c9;
  --white:#ffffff;
  --ink:#1c1c1c;
  --mid:#6d6d6d;
  --dark:#3a3a3a;
  --light:#e8e8e8;
  --rule:#9a9a9a;
}
*{box-sizing:border-box;margin:0;padding:0}
html,body{width:677px;height:1200px;overflow:hidden;background:var(--bg)}
body{position:relative;font-family:"Montserrat",sans-serif;color:var(--ink)}
.abs{position:absolute}

/* ---------- address side ---------- */
.address-side{left:177px;top:299px;width:461px;height:286px;background:var(--white);box-shadow:0 1px 4px rgba(0,0,0,.15)}
.address-side__haze{left:0;top:0;width:461px;height:200px;background:linear-gradient(180deg,#fff 0%,#f2f2f2 55%,#fff 100%)}
.portrait-frame{left:261px;top:11px;width:186px;height:165px;border:1.5px solid #b5b5b5}
.portrait-photo{left:270px;top:5px;width:168px;height:178px;background:radial-gradient(ellipse at 55% 45%,#8a8a8a 0%,#bdbdbd 45%,#eeeeee 80%)}
.brand{left:250px;top:160px;width:222px;text-align:center}
.brand__name{font-weight:500;font-size:22px;letter-spacing:.5px;color:var(--ink)}
.brand__sub{font-weight:400;font-size:6.5px;letter-spacing:3px;color:var(--ink);margin-top:1px}
.address-side__headline{left:250px;top:207px;width:222px;text-align:center;font-family:"Poppins",sans-serif;font-weight:300;letter-spacing:5px;line-height:15px}
.address-side__headline .l1{font-size:12px;color:var(--mid)}
.address-side__headline .l2{font-size:14px;color:var(--ink)}
.address-side__rule{left:340px;top:247px;width:80px;height:1px;background:#bbb}
.address-side__url{left:250px;top:254px;width:222px;text-align:center;font-size:7.5px;letter-spacing:1.4px;color:var(--ink)}

/* ---------- coupon fronts ---------- */
.coupon{left:45px;width:154px;border:1px dashed #8a8a8a;border-radius:6px;overflow:hidden}
.coupon--1{top:320px;height:83px;background:linear-gradient(90deg,#c4c4c4,#dcdcdc 60%,#efefef)}
.coupon--2{top:404px;height:76px;background:linear-gradient(90deg,#a9a9a9,#bdbdbd 60%,#d3d3d3)}
.coupon--3{top:481px;height:81px;background:linear-gradient(90deg,#6b6b6b,#7f7f7f 60%,#9a9a9a)}
.coupon__valid{left:6px;top:50%;width:60px;transform:translate(-22px,-50%) rotate(90deg);font-size:6px;line-height:7px;text-align:center;color:var(--ink)}
.coupon--3 .coupon__valid{color:var(--white)}
.coupon__title{left:37px;top:10px;font-weight:800;font-size:12.5px;line-height:13px;color:var(--ink)}
.coupon--3 .coupon__title{color:var(--white)}
.coupon__rule{left:37px;height:1px;width:30px;background:var(--ink)}
.coupon--3 .coupon__rule{background:var(--white)}
.coupon__value{left:37px;font-weight:800;font-size:20px;color:var(--dark)}
.coupon--3 .coupon__value{color:var(--light)}
.coupon__mark{left:100px;top:6px;font-size:6px;font-weight:500;color:var(--ink);text-align:center;line-height:6px}
.coupon__mark small{display:block;font-size:3px;letter-spacing:1px}
.coupon--3 .coupon__mark{color:var(--white)}
.coupon__number{left:128px;top:6px;width:10px;writing-mode:vertical-rl;font-weight:800;font-size:7px;letter-spacing:.5px;color:var(--ink)}
.coupon--3 .coupon__number{color:var(--white)}
.coupon__badge{left:137px;width:22px;height:22px;border-radius:50%;background:var(--white);font-weight:800;font-size:4.5px;line-height:5px;text-align:center;padding-top:6px;color:var(--ink);writing-mode:vertical-rl;display:flex;align-items:center;justify-content:center}

/* ---------- inside spread ---------- */
.spread{left:40px;top:616px;width:461px;height:287px;overflow:hidden;background:linear-gradient(100deg,#6c6c6c 0%,#7a7a7a 45%,#8d8d8d 75%,#a3a3a3 100%);color:var(--white)}
.spread__face{left:270px;top:0;width:191px;height:200px;background:radial-gradient(ellipse at 65% 40%,#bdbdbd 0%,#979797 40%,rgba(130,130,130,0) 75%)}
.spread__portrait{left:0;top:155px;width:114px;height:132px;background:radial-gradient(ellipse at 55% 45%,#d6d6d6 0%,#a2a2a2 45%,#6c6c6c 85%)}
.spread__products{left:258px;top:74px;width:123px;height:102px;background:linear-gradient(180deg,#4d4d4d 0%,#8a8a8a 55%,#dcdcdc 80%,#6f6f6f 100%);opacity:.9}
.intro{left:13px;top:16px}
.intro__l1{font-weight:300;font-size:15px;line-height:16px}
.intro__l2{font-weight:800;font-size:15px;line-height:16px}
.intro__sub{font-weight:500;font-size:11px;line-height:12.5px;margin-top:5px;letter-spacing:.3px}
.guide{left:13px;top:90px;font-size:6.6px;line-height:8px}
.guide__title{font-size:7.4px}
.treatments{left:13px;top:114px;font-size:6px;line-height:8px;list-style:none}
.treatments--b{left:117px}
.treatments li::before{content:"";display:inline-block;width:3px;height:3px;border:.6px solid var(--white);border-radius:50%;margin-right:2px;vertical-align:1px}
.mission{left:120px;top:171px;width:86px}
.mission__title{font-weight:800;font-size:6.8px}
.mission__body{font-size:5.2px;line-height:6.5px;margin-top:3px}
.offer{left:233px;top:14px;font-weight:900;font-size:27px;line-height:25px;color:var(--ink)}
.offer-label{left:303px;top:17px;font-size:15px;line-height:17.5px;color:var(--white)}
.offer-label b{font-weight:800}
.offer-label span{font-weight:500}
.cta{left:220px;top:183px;width:150px;text-align:center}
.cta__main{font-weight:800;font-size:17px;line-height:18px}
.cta__sub{font-size:6.5px;letter-spacing:3.8px}
.cta__icon{display:block;margin:4px auto 2px}
.cta__phone{font-weight:600;font-size:13px;letter-spacing:.3px}
.cta__note{font-size:6.8px;margin-top:2px;white-space:nowrap}
.cta__note b{font-weight:800;font-size:11px}

/* ---------- coupon backs ---------- */
.ticket{left:476px;width:156px;border:1px dashed #8a8a8a;border-radius:6px;overflow:hidden}
.ticket--1{top:638px;height:82px;background:linear-gradient(90deg,#d6d6d6,#e6e6e6)}
.ticket--2{top:721px;height:76px;background:linear-gradient(90deg,#a9a9a9,#bbbbbb)}
.ticket--3{top:798px;height:82px;background:linear-gradient(90deg,#5e5e5e,#6f6f6f);color:var(--white)}
.ticket__terms{left:27px;top:13px;width:95px}
.ticket__head{font-weight:500;font-size:4.4px}
.ticket__text{font-size:4.1px;line-height:5px;margin-top:2px}
.ticket__rule{height:.6px;background:currentColor;margin-top:4px;width:92px}
.ticket__visit{font-size:4.1px;margin-top:9px;line-height:5px}
.ticket__visit b{font-weight:600;font-size:5px}
.ticket__title{left:128px;top:6px;height:68px;width:16px;writing-mode:vertical-rl;transform:rotate(180deg);font-weight:800;font-size:6px;line-height:7px;text-align:center;border-left:.8px dashed currentColor;padding-left:3px}
</style>
</head>
<body>

<!-- address side -->
<section class="abs address-side" aria-label="Mailer address side">
  <div class="abs address-side__haze" role="img" aria-label="Soft faded beach backdrop"></div>
  <div class="abs portrait-photo" role="img" aria-label="Photo of a smiling woman in a straw hat"></div>
  <div class="abs portrait-frame"></div>
  <div class="abs brand">
    <div class="brand__name">Corva Lune</div>
    <div class="brand__sub">MEDICAL SPA</div>
  </div>
  <div class="abs address-side__headline"><div class="l1">NEW YEAR</div><div class="l2">NEW YOU!</div></div>
  <div class="abs address-side__rule"></div>
  <div class="abs address-side__url">www.corvalunemedicalspa.com</div>
</section>

<!-- coupon fronts -->
<article class="abs coupon coupon--1">
  <div class="abs coupon__valid">VALID TILL<br>30<sup>TH</sup> DECEMBER</div>
  <div class="abs coupon__title">VELQUIN<br>OR PARELLE</div>
  <div class="abs coupon__mark">Corva Lune<small>MEDICAL SPA</small></div>
  <div class="abs coupon__rule" style="top:45px"></div>
  <div class="abs coupon__value" style="top:52px">$50 OFF</div>
  <div class="abs coupon__number">COUPON 1</div>
  <div class="abs coupon__badge" style="top:56px">$50 OFF</div>
</article>
<article class="abs coupon coupon--2">
  <div class="abs coupon__valid">VALID TILL<br>30<sup>TH</sup> DECEMBER</div>
  <div class="abs coupon__title" style="top:14px">1 FILLER<br>SYRINGE</div>
  <div class="abs coupon__mark">Corva Lune<small>MEDICAL SPA</small></div>
  <div class="abs coupon__rule" style="top:45px"></div>
  <div class="abs coupon__value" style="top:48px">$75 OFF</div>
  <div class="abs coupon__number">COUPON 2</div>
  <div class="abs coupon__badge" style="top:50px">$75 OFF</div>
</article>
<article class="abs coupon coupon--3">
  <div class="abs coupon__valid">VALID TILL<br>30<sup>TH</sup> DECEMBER</div>
  <div class="abs coupon__title" style="top:14px">KX<br>PRODUCTS</div>
  <div class="abs coupon__mark">Corva Lune<small>MEDICAL SPA</small></div>
  <div class="abs coupon__rule" style="top:46px"></div>
  <div class="abs coupon__value" style="top:50px">15% OFF</div>
  <div class="abs coupon__number">COUPON 3</div>
  <div class="abs coupon__badge" style="top:55px">15% OFF</div>
</article>

<!-- inside spread -->
<section class="abs spread" aria-label="Mailer offer side">
  <div class="abs spread__face" role="img" aria-label="Faded close-up photo of a woman's face"></div>
  <div class="abs spread__portrait" role="img" aria-label="Photo of a smiling woman resting her chin on her hand"></div>
  <div class="abs spread__products" role="img" aria-label="Photo of KX skincare product boxes and tubes"></div>

  <div class="abs intro">
    <div class="intro__l1">NEW YEAR</div>
    <div class="intro__l2">NEW YOU!</div>
    <div class="intro__sub">MAKE YOUR BEAUTY DREAMS<br>A REALITY!</div>
  </div>
  <div class="abs guide">
    <div class="guide__title">Virtual Treatment Guide</div>
    <div>Discover our treatments by hovering over your area of concern.</div>
  </div>
  <ul class="abs treatments">
    <li>THESSORA – Hair growth</li>
    <li>Injectables</li>
    <li>Skin Rejuvenation</li>
    <li>Arventa RF Microneedling</li>
    <li>IPL Photorejuvenation</li>
  </ul>
  <ul class="abs treatments treatments--b">
    <li>Sclerotherapy</li>
    <li>IPL Hair Removal</li>
    <li>Massages</li>
    <li>Qelto</li>
  </ul>
  <div class="abs mission">
    <div class="mission__title">OUR MISSION</div>
    <p class="mission__body">is to achieve a younger, healthier, natural looking appearance without surgery. We are here to enhance your natural beauty. When you walk into our medical spa, the focus is on you. We promote a collaborative treatment plan between the provider and client to achieve a realistic aesthetic outcome.</p>
  </div>

  <div class="abs offer">15%<br>OFF</div>
  <div class="abs offer-label"><span>LASER HAIR</span><br><b>REMOVAL</b><br><span>PACKAGES</span></div>

  <div class="abs cta">
    <div class="cta__main">CALL TODAY</div>
    <div class="cta__sub">TO LEARN MORE</div>
    <svg class="cta__icon" width="11" height="11" viewBox="0 0 20 20" aria-hidden="true">
      <circle cx="10" cy="10" r="9" fill="none" stroke="#fff" stroke-width="1.6"/>
      <path d="M7 5.5l1.6 2.2-1 1.2c.6 1.3 1.6 2.3 2.9 2.9l1.2-1 2.2 1.6-.8 1.6c-3.5-.4-6.3-3.2-6.7-6.7z" fill="#fff"/>
    </svg>
    <div class="cta__phone">555-014-7720</div>
    <div class="cta__note">MAKE SURE TO MENTION <b>MAIL OFFER!</b></div>
  </div>
</section>

<!-- coupon backs -->
<article class="abs ticket ticket--1">
  <div class="abs ticket__terms">
    <div class="ticket__head">TERMS AND CONDITIONS</div>
    <p class="ticket__text">Lorem ipsum dolor sit amet, consectetur adipiscing elit, sed do eiusmod tempor incididunt ut labore et dolore magna aliqua. Quis ipsum suspendisse ultrices gravida.</p>
    <div class="ticket__rule"></div>
    <p class="ticket__visit">Visit us to know more<br><b>www.corvalunemedicalspa.com</b></p>
  </div>
  <div class="abs ticket__title">VELQUIN<br>OR PARELLE</div>
</article>
<article class="abs ticket ticket--2">
  <div class="abs ticket__terms">
    <div class="ticket__head">TERMS AND CONDITIONS</div>
    <p class="ticket__text">Lorem ipsum dolor sit amet, consectetur adipiscing elit, sed do eiusmod tempor incididunt ut labore et dolore magna aliqua. Quis ipsum suspendisse ultrices gravida.</p>
    <div class="ticket__rule"></div>
    <p class="ticket__visit" style="margin-top:6px">Visit us to know more<br><b>www.corvalunemedicalspa.com</b></p>
  </div>
  <div class="abs ticket__title" style="height:62px">1 FILLER<br>SYRINGE</div>
</article>
<article class="abs ticket ticket--3">
  <div class="abs ticket__terms">
    <div class="ticket__head">TERMS AND CONDITIONS</div>
    <p class="ticket__text">Lorem ipsum dolor sit amet, consectetur adipiscing elit, sed do eiusmod tempor incididunt ut labore et dolore magna aliqua. Quis ipsum suspendisse ultrices gravida.</p>
    <div class="ticket__rule"></div>
    <p class="ticket__visit">Visit us to know more<br><b>www.corvalunemedicalspa.com</b></p>
  </div>
  <div class="abs ticket__title">KX<br>PRODUCTS</div>
</article>

</body>
</html>
```